Career development coaching - school lever to adults, needs a business card

Tandem Lark - An independent Career Advice business that provides 1-2-1 advice,for career development, entrepreneurial support and workshops needs a business card. Our clients of all ages (school leaver to adults looking for a career move) and universities and colleges. We would like the card to be double-sided with a modern, professional look. Looking for something professional yet very creative and original. Want a standard size business card that inspires a second look because it stands out from the rest.

One side of the card to have a design incorporating the logo with Tandem Lark name with the strap line “Guiding you toward what's next” and space for the company website

Other side of the card to the logo/Tandem Lark name and the usual contact information:
Individual Name
Job Title (for example, Director)
Phone number
Email address
Company website address

Facebook, LinkedIn and Twitter links will need to go somewhere (back or front!)

The design will be used for 3 individuals so should be editable so that we can update as needed/as we grow.

Attached is the company logo/colours to be incorporated.

Target Market(s)

1-2-1 advice,for career development, entrepreneurial support and workshops needs a business card. Our clients of all ages (school leaver to adults looking for a career move) and universities and colleges.

Industry/Entity Type

Consulting

Contact Information for Business Card

Individual Name
Phone number
Email address
Company website address

Font styles to use
Sans Serif

Colors
0255a3
3176b5
faa54b
f78f20
85acd3
cfdeed

Requirements
Must have
• use the Tandem Lark Logo in some way - using the colours and the blue/orange palette
• For the logo - hope this makes sense to someone or if they direclty relate to the logo image attached!
• For the Orange:- Pantone 1585 C
• In CMYK : C3 M71 Y100 K0
• For the Blue:- 100% Pantone 7469 C
• In CMYK : C100 M62 Y27 K7
• Please feel free to contact me with any questions for more info
Nice to have
• happy to see any creative designs
Should not have
• Nothing too traditional,

```html
<!DOCTYPE html>
<html lang="en">
<head>
<meta charset="utf-8">
<title>Tandem Lark — Business Card</title>
<link rel="stylesheet" href="https://fonts.googleapis.com/css2?family=Open+Sans:wght@400;600&display=swap">
<style>
  :root {
    --blue: #0e6590;
    --orange: #ec7335;
    --ink: #4a4a4a;
    --paper: #ffffff;
    --rule: #c9c9c9;
    --backdrop: #6e5646;
  }
  * { margin: 0; padding: 0; box-sizing: border-box; }
  html, body {
    width: 1200px; height: 987px; overflow: hidden;
    background: var(--backdrop);
    font-family: "Open Sans", sans-serif;
  }
  .card {
    position: absolute; left: 293px; width: 615px; height: 351px;
    box-shadow: 0 2px 6px rgba(0,0,0,.35);
  }
  .card--front { top: 130px; background: var(--paper); }
  .card--back { top: 506px; background: var(--blue); }

  .social { position: absolute; top: 12px; right: 16px; display: flex; gap: 3px; }
  .social span { width: 19px; height: 19px; border-radius: 50%; background: var(--blue); }

  .brand {
    position: absolute; left: 0; width: 299px; top: 110px; height: 147px;
    display: flex; align-items: center; justify-content: center; gap: 10px;
  }
  .brand__dot { width: 26px; height: 26px; border-radius: 50%; background: var(--orange); flex: none; }
  .brand__name { font-size: 27px; font-weight: 600; color: var(--blue); letter-spacing: .5px; white-space: nowrap; }

  .divider { position: absolute; left: 299px; top: 104px; width: 1px; height: 147px; background: var(--rule); }

  .contact { position: absolute; left: 330px; top: 106px; }
  .contact__name { font-size: 22px; font-weight: 600; color: var(--blue); line-height: 1.1; }
  .contact__role { font-size: 16px; color: var(--orange); margin-top: 3px; }
  .contact__list { list-style: none; margin-top: 15px; }
  .contact__list li {
    display: flex; align-items: center; gap: 9px;
    font-size: 16px; color: var(--ink); height: 23px; white-space: nowrap;
  }
  .contact__list svg { width: 14px; height: 14px; fill: var(--blue); flex: none; }

  .front-rule { position: absolute; left: 0; right: 0; top: 322px; height: 2px; background: var(--orange); }
  .front-band { position: absolute; left: 0; right: 0; top: 327px; bottom: 0; background: var(--blue); }

  .back-brand {
    position: absolute; left: 0; right: 0; top: 140px;
    display: flex; align-items: center; justify-content: center; gap: 16px;
  }
  .back-brand__dot { width: 44px; height: 44px; border-radius: 50%; background: var(--orange); flex: none; }
  .back-brand__name { font-size: 46px; font-weight: 600; color: #fff; white-space: nowrap; }
  .tagline {
    position: absolute; left: 0; right: 0; top: 289px;
    text-align: center; font-size: 18px; color: #fff;
  }
</style>
</head>
<body>
  <section class="card card--front">
    <div class="social" aria-label="Social links"><span></span><span></span><span></span></div>
    <div class="brand">
      <span class="brand__dot"></span>
      <span class="brand__name">Tandem Lark</span>
    </div>
    <div class="divider"></div>
    <div class="contact">
      <p class="contact__name">MAYA HALE</p>
      <p class="contact__role">CEO/FOUNDER</p>
      <ul class="contact__list">
        <li><svg viewBox="0 0 24 24"><path d="M6.6 10.8a15.1 15.1 0 0 0 6.6 6.6l2.2-2.2a1 1 0 0 1 1-.25 11.4 11.4 0 0 0 3.6.57 1 1 0 0 1 1 1V20a1 1 0 0 1-1 1A17 17 0 0 1 3 4a1 1 0 0 1 1-1h3.5a1 1 0 0 1 1 1c0 1.25.2 2.45.57 3.57a1 1 0 0 1-.25 1z"/></svg>555 214 0397</li>
        <li><svg viewBox="0 0 24 24"><path d="M2 5h20v2l-10 6L2 7z M2 9l10 6 10-6v10H2z"/></svg>mhale@tandemlark.com</li>
        <li><svg viewBox="0 0 24 24"><circle cx="12" cy="12" r="10"/><path d="M2 12h20M12 2c3 3 3 17 0 20M12 2c-3 3-3 17 0 20" stroke="#fff" stroke-width="1.5" fill="none"/></svg>www.tandemlark.com</li>
      </ul>
    </div>
    <div class="front-rule"></div>
    <div class="front-band"></div>
  </section>

  <section class="card card--back">
    <div class="back-brand">
      <span class="back-brand__dot"></span>
      <span class="back-brand__name">Tandem Lark</span>
    </div>
    <p class="tagline">Guiding you toward what's next</p>
  </section>
</body>
</html>
```